Kem7Dex Letterhead

Need a new letterhead for my law firm.
IDENTIFYING INFORMATION BELOW:
Ansel T Brightwater III
Attorney at Law
Address: 4832 Tillbury Rd, Ste 250, Dallas, TX 75204
Phone: 866-402-7183
Fax: 469-583-0271
Email: kem@kem7dex.example
Website: www.kem7dex.example

Colors
0054AA
0677BA
7BADD7
CADEEF
E8F1F8

Requirements
Must have
• Logo needs to be on the letterhead, along with identifying information which is included in the project description.

```html
<!DOCTYPE html>
<html lang="en">
<head>
<meta charset="utf-8">
<title>Kem7Dex Letterhead</title>
<link href="https://fonts.googleapis.com/css2?family=Montserrat:wght@600;700&family=Open+Sans:wght@400;600&display=swap" rel="stylesheet">
<style>
  :root {
    --blue-deep: #0054AA;
    --blue: #0677BA;
    --blue-soft: #7BADD7;
    --blue-pale: #CADEEF;
    --blue-mist: #E8F1F8;
    --ink: #1d1f24;
    --text: #55595f;
    --rule: #d9dbde;
    --paper: #ffffff;
  }
  * { box-sizing: border-box; margin: 0; padding: 0; }
  html, body { width: 900px; height: 1200px; overflow: hidden; background: var(--paper); }
  body { font-family: "Open Sans", Arial, sans-serif; color: var(--text); }
  .letterhead { position: relative; width: 900px; height: 1200px; }

  .header { position: absolute; top: 96px; left: 84px; right: 84px; display: flex; justify-content: space-between; align-items: center; }
  .brand { display: flex; align-items: center; gap: 14px; }
  .brand-square { width: 30px; height: 30px; background: var(--blue); }
  .brand-name { font-family: "Open Sans", Arial, sans-serif; font-weight: 600; font-size: 36px; color: var(--ink); line-height: 1; }
  .sender { text-align: right; }
  .sender-name { font-family: "Montserrat", Arial, sans-serif; font-weight: 600; font-size: 15px; color: var(--blue-deep); }
  .sender-title { font-size: 13px; color: var(--text); margin-top: 3px; }

  .header-rule { position: absolute; top: 178px; left: 84px; right: 84px; height: 1px; background: var(--rule); }
  .header-rule::before { content: ""; position: absolute; left: 0; top: -1px; width: 250px; height: 3px; background: var(--blue); }

  .recipient { position: absolute; top: 228px; left: 84px; font-size: 12px; line-height: 1.75; }
  .recipient-name { font-family: "Montserrat", Arial, sans-serif; font-weight: 700; font-size: 14px; color: var(--ink); }
  .recipient-role { margin-bottom: 6px; }
  .recipient-line { display: flex; align-items: center; gap: 8px; }
  .recipient-line svg { width: 11px; height: 11px; fill: var(--blue); }

  .date { position: absolute; top: 322px; right: 84px; font-size: 12px; }

  .body { position: absolute; top: 372px; left: 84px; right: 84px; font-size: 13px; line-height: 1.75; }
  .body p { margin-bottom: 20px; }

  .signature { position: absolute; top: 770px; left: 84px; }
  .signature-mark { width: 130px; height: 54px; background: linear-gradient(90deg, var(--blue-mist), #eef0f2); border-radius: 4px; }
  .signature-name { font-family: "Montserrat", Arial, sans-serif; font-weight: 600; font-size: 14px; color: var(--ink); margin-top: 8px; }
  .signature-title { font-size: 12px; margin-top: 2px; }

  .footer { position: absolute; top: 1030px; left: 84px; right: 84px; border-top: 1px solid var(--rule); padding-top: 22px; display: flex; }
  .footer-item { flex: 1; display: flex; gap: 12px; font-size: 12.5px; line-height: 1.6; color: var(--ink); padding-left: 18px; border-left: 1px solid var(--rule); }
  .footer-item:first-child { padding-left: 0; border-left: none; }
  .footer-icons { display: flex; flex-direction: column; gap: 4px; padding-top: 3px; }
  .footer-icons svg { width: 14px; height: 14px; fill: var(--blue); }

  .fine-print { position: absolute; top: 1128px; left: 84px; right: 84px; font-size: 9px; text-align: center; color: #8a8e94; }
</style>
</head>
<body>
<main class="letterhead">
  <header class="header">
    <div class="brand">
      <div class="brand-square"></div>
      <div class="brand-name">Kem7Dex</div>
    </div>
    <div class="sender">
      <div class="sender-name">Ansel T Brightwater III</div>
      <div class="sender-title">Attorney at Law</div>
    </div>
  </header>
  <div class="header-rule"></div>

  <section class="recipient">
    <div class="recipient-name">Jordan Hale</div>
    <div class="recipient-role">Designer</div>
    <div class="recipient-line"><svg viewBox="0 0 12 12"><path d="M6 0a4 4 0 0 0-4 4c0 3 4 8 4 8s4-5 4-8a4 4 0 0 0-4-4zm0 5.5A1.5 1.5 0 1 1 6 2.5a1.5 1.5 0 0 1 0 3z"/></svg>New York City, Zip Code - 000</div>
    <div class="recipient-line"><svg viewBox="0 0 12 12"><circle cx="6" cy="6" r="5.5"/></svg>www.recipientsite.example</div>
    <div class="recipient-line"><svg viewBox="0 0 12 12"><path d="M2.5 0.5l2 2.5-1 1.2a7 7 0 0 0 4.3 4.3l1.2-1 2.5 2-1.3 2a10 10 0 0 1-9.7-9.7z"/></svg>+000 123 456 789</div>
  </section>

  <div class="date">Date : 20 September 2020</div>

  <section class="body">
    <p>Thank you for meeting with our office last week to review the details of your matter. We have carefully studied the documents you provided and prepared an outline of the next steps we recommend. Our aim is to resolve each open question quickly while protecting your interests at every stage of the process.</p>
    <p>In the coming weeks we will contact the other party, request the remaining records and draft a written summary of our position. You will receive copies of all correspondence so that you can follow progress and share any concerns. Please keep any new papers you receive and forward them to us without delay.</p>
    <p>Our fees remain as set out in the engagement letter, and we will send a detailed statement at the end of each month. If you have questions about billing, our staff will gladly help.</p>
    <p>Please do not hesitate to call us if anything is unclear.</p>
  </section>

  <section class="signature">
    <div class="signature-mark" role="img" aria-label="Handwritten signature of the attorney"></div>
    <div class="signature-name">Ansel T Brightwater III</div>
    <div class="signature-title">Attorney at Law</div>
  </section>

  <footer class="footer">
    <div class="footer-item">
      <div class="footer-icons"><svg viewBox="0 0 12 12"><path d="M6 0a4 4 0 0 0-4 4c0 3 4 8 4 8s4-5 4-8a4 4 0 0 0-4-4zm0 5.5A1.5 1.5 0 1 1 6 2.5a1.5 1.5 0 0 1 0 3z"/></svg></div>
      <div>4832 Tillbury Rd,<br>Ste 250, Dallas, TX 75204</div>
    </div>
    <div class="footer-item">
      <div class="footer-icons">
        <svg viewBox="0 0 12 12"><path d="M2.5 0.5l2 2.5-1 1.2a7 7 0 0 0 4.3 4.3l1.2-1 2.5 2-1.3 2a10 10 0 0 1-9.7-9.7z"/></svg>
        <svg viewBox="0 0 12 12"><path d="M3 1h6v3H3zM1 5h10v5H9V8H3v2H1zM3 9h6v3H3z"/></svg>
      </div>
      <div>866-402-7183<br>469-583-0271</div>
    </div>
    <div class="footer-item">
      <div class="footer-icons">
        <svg viewBox="0 0 12 12"><path d="M0 2h12v8H0zM1 3l5 3.5L11 3v-.2H1z" fill-rule="evenodd"/></svg>
        <svg viewBox="0 0 12 12"><circle cx="6" cy="6" r="5.5"/></svg>
      </div>
      <div>kem@kem7dex.example<br>www.kem7dex.example</div>
    </div>
  </footer>

  <div class="fine-print">All communications from this office are confidential and intended only for the named recipient.</div>
</main>
</body>
</html>
```